Creative Brief Document

Project Name – Spice & Seasoning blends

Project brief summary
- Brief summary of the project
We are excited to launch a new spice company called “Meadow’s Pure,” dedicated to providing sustainably sourced, high-quality spices and spice blends. We are currently exploring packaging materials for PET jars and gift bundle boxes.
The visual identity should convey a sense of purity, earthiness, vibrancy, and gourmet appeal, capturing the essence of spices while ensuring a global appeal.

Products

All Purpose Seasoning
Curry Powder
Beef Bouillon
Chicken Bouillon
Garlic & Herb
Jollof Rice
Seasoning Salt

Jar & Lid Details (see attached files)

- Reason behind brand name

“Meadow’s Pure” name to communicate pure, natural and REAL product.

- What are your business goals?
To show
1. authenticity of product - Pure & High-quality spices with no additives
2. Eco-consiousness (sustainability)
3. Vibrancy - Naturally rich and flavourful
4. Breath of fresh air
5. Exciting product
6. Premium product, yet accessible
7. Gain consumer confidence around transparency/honesty
8. Gain market share from established competitors, with a strong market leader for many years
9. Global market address

Target audience?

Mass market & Institutions (Hotels, restaurants etc)
Gift boxes for holidays such as Christmas

Brand positioning?
- Price point? Premium?
Accessible

Tone of Voice
- Eg friendly, fun, professional, expert, eco conscious, etc?

Tone to be elegant, vibrant and align with the idea of authenticity (realness), health and sustainability, just as nature intended it to be.

Modern, Classy and appealing to display in shelves despite the variety of kitchen decors
Pure and Fresh
Vibrant & Flavourful

Crisp labels when printed out

Competitors
- main competition?

Coastal Ember https://www.coastalembergroup.example/
Prime Pantry https://www.primepantryea.example/our-brands/prime-pantry
Vital Mi https://www.vitalmi.example/product-category/foods/

- Which brands are already out there doing a similar thing?

I like global brands such as Lorvo, Tamsen’s, Da Velloni, Quarrow Pure Salt etc

- How to stand out?

Attractive packaging

What are your key messages?
- What is the key idea the pack needs to communicate?

Real product (Authentic)
Fresh
Accessible
Beautiful
Easy to use

- Do you have a unique selling point?

100% Natural (No additives or fillers)
Sustainably sourced
Premium quality at an accessible price
Eco-friendly packaging

Packaging
- Preferred packaging structure?

**We are using pet jars to package all our products for now.
We would like a label that goes round the jar and also with a tamper seal that goes over the lid .

See these video:

Apply labels with tamper seals on Fine Mechanix's DeskPILOT label applicator (youtube.com)

Brand Name: Meadow’s Pure with logo

Unique Selling Point/ Tags: ALL Natural, No preservatives, Premium Quality

Product Name: Chicken Seasoning
(Pilipili ya Dago)

Product Picture: Stock pics
 Compact jar, more spice – less plastic waste! 🌍
 Heat levels: visual icons for 0-All flavor, No heat, 1- Mild, 2-Medium, 3-Hot
• Scan for delicious recipes: QR code for recipes
• Enjoy on: [list] Chicken, Seafood, xx, etc
• Symbols to add: Recycling, Sustainability, Eco-Friendly (Better for the environment), Low Carbon Footprint, Suitable for Vegetarians, NQAs Mark of Standardization, Product Barcode, Kenyan Flag (Made in Kenya)

Product Details:
• Ingredients: xxx
• Nutritional Facts
 About xx servings per container
 Serving size x tbsp. (x g)
 Calories per serving x
• Allergen Information
• Net wt.: g and oz – Make this section extremely visible

Company Details:

Wavecrest Dawns Co. Ltd
P.O. Box 42613, GPO 00200
Nairobi, Kenya
Tel: 07xxxxxxxx
www.wavecrestdawns.example

Storage Details:
Store in a cool and dry place

Target Market(s)

Mass market with a global appeal

Industry/Entity Type

Spices and Seasonings

Colors

Designer to choose colors to be used in the design.

Requirements
Must have
• colourful, quick to read at a glance pics and fonts. Minimal details in the front i.e. logo, spice name, heat levels, weight & centre picture
Should not have
• Hard to easily read fonts

```html
<!DOCTYPE html>
<html lang="en">
<head>
<meta charset="utf-8">
<title>Meadow's Pure – Chicken Seasoning Label</title>
<link href="https://fonts.googleapis.com/css2?family=Poppins:wght@600;700;800;900&display=swap" rel="stylesheet">
<style>
  :root {
    --canvas: #e9e9e9;
    --label: #cbbfa9;
    --brand-red: #e63a3b;
    --accent-orange: #f7a51e;
    --ink: #1d1d1d;
    --white: #ffffff;
    --wood-light: #c7925a;
    --wood-dark: #8a5a30;
    --badge: #2a2a2a;
  }
  * { box-sizing: border-box; margin: 0; padding: 0; }
  html, body { width: 1200px; height: 1200px; overflow: hidden; }
  body { background: var(--canvas); font-family: 'Poppins', sans-serif; position: relative; }

  .label {
    position: absolute; left: 327px; top: 40px;
    width: 545px; height: 1120px;
    background: var(--label);
    overflow: hidden;
  }
  .brand {
    position: absolute; left: 0; top: 44px; width: 100%; height: 60px;
    display: flex; align-items: center; justify-content: center; gap: 14px;
  }
  .brand-dot {
    width: 26px; height: 26px; background: var(--brand-red);
  }
  .brand-name {
    font-family: 'Poppins', sans-serif; font-weight: 700;
    font-size: 38px; color: var(--ink); line-height: 1;
  }
  .product-title { position: absolute; left: 0; top: 193px; width: 100%; }
  .title-highlight {
    position: absolute; left: 0; top: 0; width: 487px; height: 101px;
    background: var(--accent-orange);
  }
  .title-line {
    position: absolute; left: 6px;
    font-weight: 900; font-size: 90px; line-height: 1;
    color: var(--ink); letter-spacing: -1px; white-space: nowrap;
  }
  .title-line.chicken { top: 8px; }
  .title-line.seasoning { top: 150px; font-size: 86px; }
  .local-name {
    position: absolute; left: 6px; top: 478px;
    font-weight: 700; font-size: 40px; color: var(--ink); white-space: nowrap;
  }
  .product-photo {
    position: absolute; left: 0; top: 578px; width: 100%; height: 444px;
    background:
      linear-gradient(180deg, transparent 0 69px, var(--accent-orange) 69px 107px, transparent 107px 171px, var(--wood-light) 171px, var(--wood-dark) 100%),
      var(--label);
  }
  .quality-badge {
    position: absolute; left: 4px; top: 600px; width: 130px; height: 130px;
    border-radius: 50%; background: var(--badge);
  }
  .claims {
    position: absolute; left: 8px; top: 912px; width: 506px; height: 70px;
    background: var(--white); border-radius: 35px;
    display: flex; align-items: center; justify-content: space-around;
    font-weight: 700; font-size: 25px; color: var(--ink);
  }
  .claim { display: flex; align-items: center; gap: 8px; white-space: nowrap; }
  .claim svg { width: 30px; height: 30px; }
  .net-weight {
    position: absolute; left: 123px; top: 1060px; width: 289px; height: 48px;
    background: var(--ink); border-radius: 10px;
    display: flex; align-items: center; justify-content: center;
    font-weight: 800; font-size: 23px; color: var(--accent-orange);
  }
</style>
</head>
<body>
  <main class="label">
    <div class="brand">
      <span class="brand-dot" aria-hidden="true"></span>
      <span class="brand-name">Meadow’s Pure</span>
    </div>

    <div class="product-title">
      <div class="title-highlight"></div>
      <h1 class="title-line chicken">CHICKEN</h1>
      <h1 class="title-line seasoning">SEASONING</h1>
    </div>
    <p class="local-name">(PILIPILI YA DAGO)</p>

    <div class="product-photo" role="img" aria-label="Bowl of orange-brown seasoning powder on a wooden table"></div>
    <div class="quality-badge" aria-hidden="true"></div>

    <div class="claims">
      <span class="claim">
        <svg viewBox="0 0 30 30"><path d="M6 26 C6 12 14 4 26 4 C26 16 18 24 6 26 Z" fill="#1d1d1d"/><path d="M6 26 L18 12" stroke="#fff" stroke-width="2"/></svg>
        All Natural
      </span>
      <span class="claim">
        <svg viewBox="0 0 30 30"><path d="M15 3 C15 3 6 14 6 19 A9 9 0 0 0 24 19 C24 14 15 3 15 3 Z" fill="none" stroke="#1d1d1d" stroke-width="2"/></svg>
        No Preservatives
      </span>
    </div>

    <div class="net-weight">NT. WT. 5oz (141gr)</div>
  </main>
</body>
</html>
```